Design a New Site for a very cool Watch

We have the overall design element of the website and the banners in the PSD file. We need someone to finish our design in PSD and than convert to HTML. We have included the instructions, PSD file, images and all text.

We currently use Hubspot to host and make changes to our site. The entire design aspect is complete so all we need is some minor changes and additions within the photoshop design and than the coding into HTML.

Please only sign up if you understand photoshop and HTML conversion

Here is the DropBox link to the files
https://files.quorvel-share.net/s/pm4kx82lwq7dtne/Belthor%20Site.zip
Updates

We have the basic design concept in Photoshop.  We just need someone who can complete some changes, make some additions and convert to HTML

Target Market(s)

Watch Buyers

Requirements
Must have
• Must look like a professional luxury brand

Our brand colors are very basic with Black, White and Grey can be used

```html
<!DOCTYPE html>
<html lang="en">
<head>
<meta charset="utf-8">
<title>Belthor &amp; Co. — The Lyra Watch Collection</title>
<link href="https://fonts.googleapis.com/css2?family=Ubuntu:wght@400;500&family=Noto+Sans:wght@400&family=Dancing+Script:wght@700&display=swap" rel="stylesheet">
<style>
:root{
  --green:#7aab1c;
  --green-text:#6d9a1e;
  --header-bg:#eef3dc;
  --dash:#b9d27a;
  --ink:#1c1c1c;
  --teal:#5bacaa;
  --rust:#c8461e;
  --rule-blue:#2d6ea6;
  --body-grey:#555;
  --footer-bg:#f0ede8;
  --footer-grey:#8a8a8a;
  --hero-a:#c3b1a3;
  --hero-b:#d2c6bc;
}
*{box-sizing:border-box;margin:0;padding:0}
html,body{width:1097px;height:1200px;overflow:hidden;background:#fff}
body{font-family:"Noto Sans",sans-serif;color:var(--ink)}
.page{position:relative;width:1097px;height:1200px;overflow:hidden}
.abs{position:absolute}

/* header */
.site-header{position:absolute;left:0;top:0;width:1097px;height:120px;background:var(--header-bg);border-top:3px solid var(--green)}
.site-header .dash{position:absolute;left:0;width:100%;border-top:1px dashed var(--dash)}
.brand{position:absolute;left:147px;top:40px;height:40px;display:flex;align-items:center;gap:12px}
.brand-mark{width:34px;height:34px;background:var(--ink)}
.brand-name{font-family:"Ubuntu",sans-serif;font-size:25px;font-weight:400;color:var(--ink);letter-spacing:.5px;border-left:1px solid var(--ink);padding-left:12px;line-height:36px}
.utility{position:absolute;top:30px;font-family:"Ubuntu",sans-serif;font-size:13px;color:var(--ink)}
.utility .cart-label{color:var(--green)}
.main-nav{position:absolute;top:59px;left:424px;font-family:"Ubuntu",sans-serif;font-size:14px}
.main-nav a{position:absolute;top:0;height:28px;line-height:28px;color:var(--green-text);text-decoration:none;white-space:nowrap}
.main-nav a.active{background:#8c9a7c;color:#fff;width:63px;text-align:center;border-radius:2px}

/* hero */
.hero{position:absolute;left:0;top:120px;width:1097px;height:314px;background:linear-gradient(90deg,var(--hero-a),var(--hero-b) 45%,var(--hero-a))}
.hero-watch{position:absolute;left:180px;top:0;width:278px;height:314px;background:radial-gradient(ellipse at 55% 45%,#6f7f96 0%,#2c3a5e 40%,#1b2340 70%,rgba(27,35,64,0) 72%)}
.hero-copy{position:absolute;left:542px;color:#fff;font-family:"Ubuntu",sans-serif;text-shadow:0 1px 2px rgba(0,0,0,.35)}
.hero-title{top:56px;font-size:29px;line-height:38px}
.hero-lede{top:152px;font-size:12.5px;line-height:15px;font-family:"Noto Sans",sans-serif;width:400px}
.hero-limit{top:214px;font-size:19px;line-height:27px}

/* welcome */
.welcome{position:absolute;left:0;top:458px;width:1097px;text-align:center;font-family:"Ubuntu",sans-serif;font-size:29px;color:var(--ink)}
.welcome span{color:var(--green)}
.welcome-rule{position:absolute;left:289px;top:510px;width:530px;height:1px;background:linear-gradient(90deg,rgba(0,0,0,0),#ccc,rgba(0,0,0,0))}

/* feature cards */
.card{position:absolute;top:536px;width:194px;height:314px;border:1px solid #e6e6e6;background:#fff;box-shadow:0 3px 0 -1px #eee}
.card-title{position:absolute;left:0;top:14px;width:100%;text-align:center;font-family:"Ubuntu",sans-serif;font-size:17px;line-height:20px;color:var(--teal)}
.card-title em{font-style:normal;color:var(--rust)}
.card-rule{position:absolute;left:9px;top:83px;width:176px;height:2px;background:var(--rule-blue)}
.card-image{position:absolute;left:9px;top:100px;width:177px;height:88px}
.card-text{position:absolute;left:9px;top:191px;width:178px;font-size:10px;line-height:14.5px;color:var(--body-grey)}
.card-more{position:absolute;left:124px;top:269px;width:60px;height:19px;background:var(--rust);color:#fff;font-family:"Ubuntu",sans-serif;font-size:12px;line-height:19px;text-align:center}

/* footer */
.site-footer{position:absolute;left:0;top:896px;width:1097px;height:254px;background:var(--footer-bg);border-top:1px solid #e4e1dc}
.footer-heading{position:absolute;top:28px;font-family:"Ubuntu",sans-serif;font-size:24px;color:var(--ink)}
.footer-links{position:absolute;left:149px;top:80px;list-style:none;font-size:10px;line-height:16px;color:var(--footer-grey)}
.footer-text{position:absolute;font-size:10px;line-height:16px;color:var(--footer-grey)}
.email-label{position:absolute;left:390px;top:145px;font-size:10px;color:#333}
.email-input{position:absolute;left:389px;top:158px;width:225px;height:26px;background:#fff;border:1px solid #c9c9c9;border-radius:3px}
.submit{position:absolute;left:541px;top:198px;width:70px;height:22px;background:linear-gradient(#8fd04a,#5ea91c);color:#fff;font-size:10px;line-height:22px;text-align:center;border-radius:2px;box-shadow:0 1px 2px rgba(0,0,0,.25)}
.contact-icon{position:absolute;width:20px;height:20px}

/* bottom bar */
.legal{position:absolute;left:149px;top:1170px;font-size:9.5px;color:#555}
.follow{position:absolute;left:807px;top:1161px;font-family:"Dancing Script",cursive;font-size:19px;color:var(--green)}
.social{position:absolute;top:1163px;width:16px;height:16px;background:#8a8a8a;border-radius:2px}
</style>
</head>
<body>
<div class="page">

  <header class="site-header">
    <div class="dash" style="top:10px"></div>
    <div class="dash" style="top:106px"></div>

    <div class="brand">
      <div class="brand-mark"></div>
      <div class="brand-name">BELTHOR &amp; CO.</div>
    </div>

    <svg class="abs" style="left:644px;top:30px" width="18" height="13" viewBox="0 0 18 13"><rect x="0" y="0" width="18" height="13" fill="#222"/><path d="M0 0 L9 7 L18 0" stroke="#eef3dc" stroke-width="1.5" fill="none"/></svg>
    <div class="utility" style="left:671px">shop.belthor.com</div>
    <svg class="abs" style="left:783px;top:29px" width="20" height="16" viewBox="0 0 20 16"><path d="M0 1 H4 L6 10 H16 L18 3 H5" stroke="#222" stroke-width="1.6" fill="none"/><circle cx="7" cy="13.5" r="1.6" fill="#222"/><circle cx="15" cy="13.5" r="1.6" fill="#222"/></svg>
    <div class="utility" style="left:811px"><span class="cart-label">Cart:</span> 0 item(s) - $0.00</div>

    <nav class="main-nav">
      <a class="active" style="left:0">Home</a>
      <a style="left:73px">About Us</a>
      <a style="left:147px">Contact</a>
      <a style="left:222px">Collecation</a>
      <a style="left:321px">LifeStyle</a>
      <a style="left:393px">Media</a>
      <a style="left:459px">Shop Now</a>
    </nav>
  </header>

  <section class="hero">
    <div class="hero-watch" role="img" aria-label="Photograph of a square steel watch with a navy strap and dark starry dial"></div>
    <h1 class="hero-copy hero-title" style="font-weight:400">Time &amp; Space Fused Together<br>The Lyra Watch Collecation</h1>
    <p class="hero-copy hero-lede">Worlda first watch with a piece of the Moon, Mars and a rare space Gem set underneath multiple floating diamonds</p>
    <p class="hero-copy hero-limit">Entire Collection<br>Limited to 600 Pieces</p>
  </section>

  <h2 class="welcome" style="font-weight:400">welcome to our <span>Belthor &amp; Co.!</span></h2>
  <div class="welcome-rule"></div>

  <article class="card" style="left:146px">
    <h3 class="card-title" style="font-weight:400">The Lyra<br><em>Story</em></h3>
    <div class="card-rule"></div>
    <div class="card-image" role="img" aria-label="Photograph of a white-dial watch on a black background" style="background:linear-gradient(120deg,#111 10%,#8d8a8f 40%,#e8e4ea 55%,#444 80%,#111)"></div>
    <p class="card-text">Lorem Ipsum is simply dummy text of the printing and typesetting industry. Lorem Ipsum has been the industry's standard dummy text</p>
    <div class="card-more">More</div>
  </article>

  <article class="card" style="left:348px">
    <h3 class="card-title" style="font-weight:400">Register Your<br><em>Watch</em></h3>
    <div class="card-rule"></div>
    <div class="card-image" role="img" aria-label="Photograph of a red-dial watch on a black background" style="background:linear-gradient(120deg,#111 10%,#c81a1a 40%,#ff3a2a 60%,#2a0a0a 85%)"></div>
    <p class="card-text">Lorem Ipsum is simply dummy text of the printing and typesetting industry. Lorem Ipsum has been the industry's standard dummy text</p>
    <div class="card-more">More</div>
  </article>

  <article class="card" style="left:550px">
    <h3 class="card-title" style="font-weight:400">Repair, Maintenance<br><em>&amp;<br>Warranty Info</em></h3>
    <div class="card-rule"></div>
    <div class="card-image" role="img" aria-label="Image of a glowing blue planet edge in deep space" style="background:radial-gradient(ellipse at 72% 45%,#d8f2ff 0%,#3fa6e0 15%,#0c3c70 35%,#020814 65%)"></div>
    <p class="card-text">Lorem Ipsum is simply dummy text of the printing and typesetting industry. Lorem Ipsum has been the industry's standard dummy text</p>
    <div class="card-more">More</div>
  </article>

  <article class="card" style="left:754px">
    <h3 class="card-title" style="font-weight:400">Register to find out<br><em>about new watch<br>collection</em></h3>
    <div class="card-rule"></div>
    <div class="card-image" role="img" aria-label="Photograph of a navy watch with a dark starry dial" style="background:linear-gradient(120deg,#0a0d18 10%,#2a3a66 40%,#6d7890 55%,#1a2244 80%,#05070e)"></div>
    <p class="card-text">Lorem Ipsum is simply dummy text of the printing and typesetting industry. Lorem Ipsum has been the industry's standard dummy text</p>
    <div class="card-more">More</div>
  </article>

  <footer class="site-footer">
    <h4 class="footer-heading" style="left:147px;font-weight:400">Link</h4>
    <ul class="footer-links">
      <li>Contact Us</li>
      <li>Terma Of Service</li>
      <li>Refund Policy</li>
      <li>Privacy Policy</li>
    </ul>

    <svg class="abs" style="left:386px;top:35px" width="24" height="20" viewBox="0 0 24 20"><g stroke="#666" stroke-width="1.6"><path d="M2 2 H20"/><path d="M6 6 H20"/><path d="M2 10 H20"/><path d="M6 14 H20"/></g><path d="M8 18 H22" stroke="#e08a2a" stroke-width="1.6"/></svg>
    <h4 class="footer-heading" style="left:425px;font-weight:400">Newsletter Signup</h4>
    <p class="footer-text" style="left:389px;top:80px;width:220px">Cras volutpat, ante ac gravida iaculis, dui lacus iaculis nibh, eu scelerisque arcu diam a augue. Donec imperdiet pharetra fringilla.</p>
    <div class="email-label">Your Email Address</div>
    <div class="email-input"></div>
    <div class="submit">Submit</div>

    <svg class="abs" style="left:743px;top:32px" width="30" height="24" viewBox="0 0 30 24"><rect x="1" y="1" width="28" height="22" rx="2" fill="#fff" stroke="#777" stroke-width="1.5"/><path d="M1 2 L15 13 L29 2 M1 22 L11 11 M29 22 L19 11" stroke="#777" stroke-width="1.5" fill="none"/></svg>
    <h4 class="footer-heading" style="left:783px;font-weight:400">Contact Us</h4>

    <svg class="contact-icon" style="left:746px;top:83px" viewBox="0 0 20 20"><path d="M2 7 Q10 1 18 7 L16 9 L13 7 L7 7 L4 9 Z" fill="#777"/><rect x="4" y="10" width="12" height="8" rx="1" fill="#888"/></svg>
    <p class="footer-text" style="left:799px;top:88px">40012368957</p>

    <svg class="contact-icon" style="left:747px;top:133px" viewBox="0 0 20 20"><rect x="5" y="1" width="10" height="7" fill="#aaa"/><rect x="1" y="8" width="18" height="8" rx="1" fill="#888"/><rect x="5" y="14" width="10" height="5" fill="#bbb"/></svg>
    <p class="footer-text" style="left:797px;top:140px">3105.62840.17 / 555.204.118</p>
  </footer>

  <p class="legal">All Rights Reserved © Belthor &amp; Co™</p>
  <div class="follow">Follow Us</div>
  <div class="social" style="left:903px" aria-label="Social profile"></div>
  <div class="social" style="left:927px" aria-label="Social profile"></div>

</div>
</body>
</html>
```